Maren Holt Luxury Wellness Profile Booklet

I am a luxury wellness property agent and would like to create my personal profile booklet. I want this to feel luxurious, minimalist, informative and the philosophy behind wellness and property the cPAGE 1 — THE COVER

Very minimal.

MAREN HOLT

LUXURY WELLNESS PROPERTY

PROPERTY • WELLNESS • LIFESTYLE

Fenwick Dale Coastline Group

Large photograph of you — preferably walking through a beautiful waterfront property or standing naturally within an architectural setting.

At the bottom:

Kestrel Isle • Linden Cove • Ashvale

Small Fenwick Dale logo.

PAGE 2 — THE OPENING STATEMENT

A beautiful full-page lifestyle photograph.

Overlaid:

WHERE PROPERTY
MEETS WELLBEING

“A home is more than an address. It is the environment in which life unfolds.”

Then a short introduction:

Opening Profile

I believe the most exceptional properties are not defined simply by their architecture, address or price.

They are defined by how they make you feel.

Natural light. Water views. Privacy. Green space. Indoor-outdoor living. A place to unwind, entertain, recharge and reconnect.

My approach to luxury property brings these elements together — combining strategic real estate expertise with a genuine understanding of wellness, lifestyle and the way people want to live today.

Because when we understand the lifestyle behind the property, we can create a more compelling story around it.

PAGE 3 — MEET MAREN

Large portrait of you on one side.

Other side:

MEET MAREN

20+ YEARS OF PROPERTY EXPERIENCE

Commercial
Residential
Project Sales
Luxury & Lifestyle Property

Then:

About Maren

With more than 20 years' experience across commercial, residential and project sales, I have built my career around relationships, strategic marketing and delivering exceptional outcomes for my clients.

My approach is warm, considered and highly personal.

I believe sellers deserve more than a listing campaign. They deserve a clear strategy, honest communication and an agent who understands what makes their property valuable — both financially and emotionally.

Today, my focus is luxury lifestyle property across the Northern Amber Coast, with a particular passion for Kestrel Isle, Linden Cove and selected waterfront gated estates in Ashvale.

PAGE 4 — WHY WELLNESS?

This is where your differentiation becomes really powerful.

Full-bleed photograph of:

pool
outdoor entertaining
greenery
water
spa
wellness room
person walking beside water
WELLNESS IS THE NEW LUXURY

Then:

Wellness Philosophy

Luxury has evolved.

Today, luxury is not only about beautiful finishes, expansive living spaces or an impressive address.

It is privacy.

It is waking to water.

It is natural light flooding through the home.

It is having space to breathe.

It is stepping outside into nature, walking along the water, enjoying a morning swim, entertaining beside the pool or creating a private sanctuary at home.

These lifestyle elements increasingly shape the way buyers experience and value a property.

This is where my passion for wellness becomes part of my property approach.

PAGE 5 — MY WELLNESS JOURNEY

This page makes the wellness positioning credible rather than simply being a marketing slogan.

MY WELLNESS JOURNEY

You could use 3 small photographs:

BLOOMTOT CO
SOLACE WELLNESS CENTRE
LUXURY WELLNESS PROPERTY

Copy:

Wellness Journey

My connection with wellness began outside of real estate.

After stepping away from property, I founded Bloomtot Co, developing an organic children's nutritional product with a focus on natural ingredients and wellbeing.

I later launched Solace Wellness Centre, further deepening my understanding of wellness, health-conscious lifestyles and the importance of creating environments that support how we live.

Today, I bring that perspective back into property.

I see homes differently — not simply as buildings, but as environments for living, restoring, entertaining and thriving.

PAGE 6 — THE MAREN HOLT DIFFERENCE

This should be one of your strongest pages.

A DIFFERENT WAY OF SEEING PROPERTY

Use six elegant icons or small images:

01 — LIFESTYLE

I look beyond the floor plan to understand how buyers will actually experience the home.

02 — WELLNESS

I identify the spaces and features that contribute to wellbeing and lifestyle.

03 — PRESENTATION

I create a campaign that makes the property feel aspirational, memorable and emotionally engaging.

04 — STORY

Every exceptional property has a story. I find it, refine it and communicate it.

05 — STRATEGY

From positioning and buyer targeting to campaign execution and negotiation, every element has a purpose.

06 — RELATIONSHIPS

Trust, transparency and communication remain at the centre of every campaign.

PAGE 7 — YOUR PROPERTY STORY

This could be a beautiful editorial spread.

EVERY HOME HAS A STORY

Then:

My role is to discover what makes yours extraordinary.

Three questions:

WHAT MAKES YOUR PROPERTY DIFFERENT?

Architecture?
Waterfront?
Views?
Privacy?
Garden?
Location?

HOW DOES IT MAKE PEOPLE FEEL?

Calm?
Inspired?
Connected?
Entertained?
Relaxed?

WHO WILL FALL IN LOVE WITH IT?

Families?
Executives?
Downsizers?
Boaties?
Golfers?
Wellness-focused buyers?
Lifestyle purchasers?

Then:

I turn these answers into your property's story.

PAGE 8 — YOUR NORTHERN AMBER COAST

Beautiful aerial/waterfront image.

MY MARKET

KESTREL ISLE

LINDEN COVE

ASHVALE

WATERFRONT & GATED ESTATES

Copy:

Northern Amber Coast

I specialise in the lifestyle-driven property market of the Northern Amber Coast.

From the waterfront homes and private enclaves of Kestrel Isle and Linden Cove to the established gated estates of Ashvale, I understand the lifestyle characteristics that attract buyers to this part of the Amber Coast.

Having personally experienced the lifestyle of these communities, I understand that buyers are often purchasing far more than a house.

They are buying a way of life.

PAGE 9 — THE WELLNESS PROPERTY

This could become your signature page.

WHAT MAKES A WELLNESS HOME?

Use a sophisticated grid:

WATER
Pools • Waterfront • Marina • Water views

NATURE
Green space • Gardens • Reserve outlooks • Walking trails

LIGHT
Natural light • Orientation • Open spaces

MOVEMENT
Walking • Golf • Boating • Outdoor living

RESTORATION
Spa • Sauna • Cold plunge • Retreat spaces

CONNECTION
Entertaining • Family • Indoor/outdoor living

Bottom:

The most desirable luxury is often the way a home makes you feel.

PAGE 10 — THE SELLING EXPERIENCE
YOUR HOME. YOUR STORY. YOUR CAMPAIGN.

I would make this a simple six-stage journey:

01 — DISCOVER
Understand your property, your goals and your lifestyle.

↓

02 — POSITION
Establish the property's unique market position.

↓

03 — PREPARE
Presentation, styling and strategic recommendations.

↓

04 — CREATE
Photography, film, editorial storytelling and digital marketing.

↓

05 — CONNECT
Targeted buyer engagement and database activation.

↓

06 — NEGOTIATE
Strategic negotiation designed to maximise the opportunity.

PAGE 11 — THE POWER OF PRESENTATION

Large before/after style photography.

FIRST IMPRESSIONS ARE EVERYTHING

Copy:

We don't get a second opportunity to create a first impression.

Then explain your approach to:

styling
photography
cinematic video
twilight imagery
aerial photography
lifestyle storytelling
digital advertising
targeted database marketing
buyer follow-up
auction strategy

Importantly, don't make this page feel like a generic list of marketing products.

Frame everything around:

Creating desire before creating urgency.
PAGE 12 — PROVEN RESULTS

Now introduce your actual results.

RESULTS THAT BUILD CONFIDENCE

Use your strongest results as elegant case studies.

For example:
4183 Palmetto Drive, Kestrel Isle
$3,850,000
34 Days On The Market

$2.90M
71 Heron Bay Boulevard, Ashvale
Sold within 45 days

Include your result and the property's story.

$2.15M

3/9 Heron Bay Boulevard

Waterfront Villa

Then potentially:

28 DAYS

5419 Quaywood Boulevard, Kestrel Isle

Under contract following relaunch

If a result subsequently changed because the contract fell through, be careful about how you describe the current status. We can make this page completely accurate to the final outcome.

PAGE 13 — THE FENWICK DALE ADVANTAGE

This is where you let the brand support you, rather than letting the booklet become a Fenwick Dale corporate brochure.

PERSONAL SERVICE.
NATIONAL REACH.

Then a short statement about your Fenwick Dale platform.

You could include:

POWERFUL BUYER DATABASE

LUXURY PROPERTY MARKETING

AUCTION EXPERTISE

DIGITAL REACH

LOCAL KNOWLEDGE

NATIONAL NETWORK

And a short line:

The personal attention of a specialist agent, supported by the strength of a globally recognised property network.

PAGE 14 — WHAT YOU CAN EXPECT FROM ME

This page is very important for your seller proposition.

MY PROMISE TO YOU

TRANSPARENCY

Clear advice, honest feedback and no unnecessary promises.

COMMUNICATION

You will know what is happening throughout your campaign.

STRATEGY

Every decision is made with your property, market and objectives in mind.

ATTENTION TO DETAIL

Your home deserves meticulous preparation and presentation.

PERSONAL SERVICE

You deal directly with me throughout your campaign.

RESULT FOCUS

My role is to create the strongest possible environment for a successful sale.

PAGE 15 — THE CLOSING PAGE

This should be very luxurious and emotional.

Beautiful photograph of water at sunset / luxury pool / Kestrel Isle lifestyle.

YOUR HOME.
YOUR NEXT CHAPTER.

Then:

Closing Statement

Selling a home is rarely just a transaction.

It is the closing of one chapter and the beginning of another.

My role is to make the journey feel considered, strategic and personal — while creating the strongest possible opportunity for your property in the marketplace.

Thank you for considering me to represent your home.

I would be honoured to tell its story.

Then your details:

MAREN HOLT

Luxury Wellness Property

0412 557 830

BACK COVER

Keep it extremely clean.

Your photograph or perhaps a beautiful Amber Coast waterfront image.

MAREN HOLT

LUXURY WELLNESS PROPERTY

0412 557 830

Fenwick Dale logoollaboration. I can send a full brief if required.

Target Market(s)

Luxury Property Owners

Industry/Entity Type

Wellness Luxury Real Estate Lifestyle

Requirements
Must have
• A luxurious minimalist clean feel

```html
<!DOCTYPE html>
<html lang="en">
<head>
<meta charset="utf-8">
<title>Maren Holt — Luxury Wellness Property Profile</title>
<link rel="stylesheet" href="https://fonts.googleapis.com/css2?family=Cormorant+Garamond:ital,wght@0,400;0,500;1,400;1,500&family=Montserrat:wght@400;500;600;700&display=swap">
<style>
:root{
  --canvas:#000000;
  --navy:#171920;
  --navy-deep:#12141a;
  --panel:#20232b;
  --gold:#b38b57;
  --cream:#f8f5f0;
  --paper:#ffffff;
  --ink-light:#e4e1dc;
  --ink-soft:#a9a7a3;
  --ink-dark:#26262a;
  --ink-mute:#77767a;
  --line-light:#e6e1d9;
}
*{box-sizing:border-box;margin:0;padding:0}
html,body{width:1200px;height:2697px;overflow:hidden;background:var(--canvas)}
body{position:relative;font-family:"Montserrat",Arial,sans-serif;color:var(--ink-light)}
.page,.spread{position:absolute;overflow:hidden}
.abs{position:absolute}
.dark{background:var(--navy);color:var(--ink-light)}
.light{background:var(--cream);color:var(--ink-dark)}
.serif{font-family:"Cormorant Garamond",Georgia,serif}
.title{font-family:"Cormorant Garamond",Georgia,serif;font-weight:400;text-transform:uppercase;letter-spacing:.05em;line-height:1.05}
.title em{color:var(--gold);font-style:italic}
.italic-line{font-family:"Cormorant Garamond",Georgia,serif;font-style:italic;line-height:1.45}
.label{font-family:"Montserrat",Arial,sans-serif;font-weight:700;text-transform:uppercase;letter-spacing:.14em;font-size:4.3px;line-height:1.5}
.label.gold{color:var(--gold)}
.copy{font-size:4.4px;line-height:1.6}
.copy p+p{margin-top:4px}
.copy b{font-weight:700}
.num{font-family:"Cormorant Garamond",Georgia,serif;color:var(--gold);font-size:9px;line-height:1}
.tile{position:absolute;background:var(--panel);padding:6px}
.tile.on-light{background:var(--paper);border:1px solid var(--line-light)}
.tile .label{margin:4px 0 3px}
.tile .copy{color:var(--ink-soft)}
.tile.on-light .copy{color:var(--ink-mute)}
.photo{position:absolute}
.diff-item{display:flex;gap:6px;margin-bottom:5px}
.diff-item .copy{color:var(--ink-mute)}
.price-tag{position:absolute;left:5px;top:6px;background:var(--paper);color:var(--gold);padding:1px 3px}
.service-grid{display:grid;grid-template-columns:1fr 1fr;gap:5px}
.service-grid .tile{position:relative;padding:5px;height:28px;display:flex;gap:4px}
.service-grid .label{margin:0;font-size:3.6px}
</style>
</head>
<body>

<!-- Front cover -->
<section class="page cover" style="left:57px;top:105px;width:247px;height:343px;background:var(--paper)">
  <div class="photo" role="img" aria-label="Portrait of Maren walking down a bright white staircase in a light-filled home" style="left:0;top:0;width:247px;height:343px;background:radial-gradient(ellipse at 55% 55%,#d8cfc6 0%,#ece7e1 30%,#f7f4f0 60%,#ffffff 85%)"></div>
  <h1 class="abs title" style="left:0;top:18px;width:247px;text-align:center;font-size:24px;color:var(--ink-dark);letter-spacing:.09em">MAREN HOLT</h1>
  <div class="abs label gold" style="left:0;top:52px;width:247px;text-align:center;font-size:5.4px;letter-spacing:.3em">Luxury Wellness Property</div>
  <div class="abs label" style="left:0;top:331px;width:247px;text-align:center;font-size:3.8px;color:var(--ink-dark);letter-spacing:.3em">Property &nbsp;·&nbsp; Wellness &nbsp;·&nbsp; Lifestyle</div>
</section>

<!-- Spread: opening statement + meet Maren -->
<section class="spread" style="left:59px;top:507px;width:490px;height:337px">
  <div class="page dark" style="left:0;top:0;width:246px;height:337px">
    <div class="photo" role="img" aria-label="Modern black and white home at dusk beneath a large tree" style="left:0;top:0;width:246px;height:130px;background:linear-gradient(180deg,#4a4f57 0%,#2c3038 55%,var(--navy) 100%)"></div>
    <p class="abs italic-line" style="left:17px;top:135px;width:215px;font-size:15px;line-height:1.3">“A home is more than an address. It is the environment in which life unfolds.”</p>
    <div class="abs copy" style="left:17px;top:203px;width:100px">I believe the most exceptional properties are not defined simply by their architecture, address or price.</div>
    <p class="abs italic-line" style="left:17px;top:234px;width:100px;font-size:10.5px;line-height:1.3">“They are defined by how they make you feel.”</p>
    <div class="abs copy" style="left:128px;top:203px;width:103px">
      <p>From abundant natural light and tranquil water views to total privacy, lush green spaces and seamless indoor–outdoor living, the home is a place to unwind, entertain, recharge and reconnect.</p>
      <p>My approach to luxury property brings these elements together — combining strategic real estate expertise with a genuine understanding of wellness, lifestyle and the way people want to live today.</p>
      <p><b><i>Because when we understand the lifestyle behind the property, we can create a more compelling story around it.</i></b></p>
    </div>
  </div>
  <div class="photo" role="img" aria-label="Portrait of Maren seated in a white shirt and cream trousers" style="left:246px;top:0;width:114px;height:337px;background:linear-gradient(160deg,#efe9e3 0%,#e4dbd2 45%,#d9cfc5 100%)"></div>
  <div class="page light" style="left:360px;top:0;width:130px;height:337px">
    <h2 class="abs title" style="left:13px;top:22px;font-size:15px">MEET MAREN</h2>
    <div class="abs label gold" style="left:13px;top:40px;font-size:3.7px">20+ Years of Property<br>Experience</div>
    <div class="abs label gold" style="left:13px;top:58px;width:105px;font-size:3.7px">Specialising in commercial, residential, project sales &amp; luxury lifestyle property</div>
    <div class="abs copy" style="left:13px;top:110px;width:105px">
      <p>With more than 20 years' experience across commercial, residential and project sales, I have built my career around relationships, strategic marketing and delivering exceptional outcomes for my clients.</p>
      <p>My approach is warm, considered and highly personal.</p>
      <p>I believe sellers deserve more than a listing campaign. They deserve a clear strategy, honest communication and an agent who understands what makes their property valuable — both financially and emotionally.</p>
      <p>Today, my focus is luxury lifestyle property across the Northern Amber Coast, with a particular passion for <b>Kestrel Isle</b>, <b>Linden Cove</b> and selected waterfront gated estates in <b>Ashvale</b>.</p>
    </div>
  </div>
</section>

<!-- Spread: wellness is the new luxury + wellness journey -->
<section class="spread" style="left:605px;top:506px;width:498px;height:342px">
  <div class="page dark" style="left:0;top:0;width:250px;height:342px">
    <h2 class="abs title" style="left:17px;top:17px;font-size:14.5px">WELLNESS IS THE <em>NEW</em><br><em>LUXURY</em></h2>
    <div class="photo" role="img" aria-label="Infinity pool overlooking water at sunset" style="left:17px;top:60px;width:85px;height:121px;background:linear-gradient(180deg,#caa16a 0%,#8a6a4e 35%,#3f5d70 70%,#2b4d62 100%)"></div>
    <div class="photo" role="img" aria-label="Warm timber wellness room" style="left:107px;top:60px;width:61px;height:57px;background:linear-gradient(160deg,#c9b093,#8d7257)"></div>
    <div class="photo" role="img" aria-label="Pool terrace with greenery" style="left:173px;top:60px;width:60px;height:57px;background:linear-gradient(160deg,#7fa3b5,#5d7f5a)"></div>
    <div class="photo" role="img" aria-label="Spa products and pink flowers" style="left:107px;top:122px;width:61px;height:59px;background:linear-gradient(160deg,#eae6e2,#d8b8c0)"></div>
    <p class="abs italic-line" style="left:17px;top:210px;font-size:17px;line-height:1.1">Luxury has<br>evolved.</p>
    <div class="abs copy" style="left:17px;top:254px;width:120px">
      <p>Today, luxury is not only about beautiful finishes, expansive living spaces or an impressive address.</p>
      <p>It is stepping outside into nature, walking along the water, enjoying a morning swim, entertaining beside the pool or creating a private sanctuary at home.</p>
    </div>
    <div class="tile" style="left:150px;top:220px;width:83px;height:80px;padding:7px">
      <p class="italic-line" style="font-size:6.3px;color:var(--ink-light)">“These lifestyle elements increasingly shape the way buyers experience and value a property.”</p>
      <p class="copy" style="margin-top:6px;color:var(--ink-light)">This is where my passion for wellness becomes part of my property approach.</p>
    </div>
  </div>
  <div class="page light" style="left:250px;top:0;width:248px;height:226px">
    <h2 class="abs title" style="left:17px;top:17px;font-size:16px">MY <em>WELLNESS</em><br>JOURNEY</h2>
    <div class="photo" role="img" aria-label="Mother and child preparing healthy food in a kitchen" style="left:17px;top:66px;width:67px;height:84px;background:linear-gradient(170deg,#f0ebe5,#d9c7b4)"></div>
    <div class="photo" role="img" aria-label="Calm wellness centre treatment room" style="left:91px;top:66px;width:67px;height:84px;background:linear-gradient(170deg,#c6a98a,#8a6d50)"></div>
    <div class="photo" role="img" aria-label="Maren relaxing in a bright white interior" style="left:164px;top:66px;width:67px;height:84px;background:linear-gradient(170deg,#f4f1ec,#ddd5cc)"></div>
    <div class="tile on-light" style="left:17px;top:150px;width:67px;height:66px;padding:5px">
      <div class="label" style="color:var(--ink-dark)">Bloomtot Co</div>
      <div class="copy">Founder of an organic children's nutritional brand focused on clean, natural ingredients.</div>
    </div>
    <div class="tile on-light" style="left:91px;top:150px;width:67px;height:66px;padding:5px">
      <div class="label" style="color:var(--ink-dark)">Solace Wellness Centre</div>
      <div class="copy">Created a sanctuary for health-conscious living and physical wellness environments.</div>
    </div>
    <div class="tile on-light" style="left:164px;top:150px;width:67px;height:66px;padding:5px">
      <div class="label" style="color:var(--ink-dark)">Luxury Wellness Property</div>
      <div class="copy">Integrating 20+ years of property expertise with a deep understanding of wellness lifestyle.</div>
    </div>
  </div>
  <div class="page dark" role="img" aria-label="Faint interior photograph behind the text" style="left:250px;top:226px;width:248px;height:116px;background:linear-gradient(180deg,#22252d,#1b1d24)"></div>
  <div class="abs copy" style="left:267px;top:246px;width:95px">
    <p style="color:var(--gold)"><b>My passion for wellness is deeply personal.</b></p>
    <p>As the founder of Bloomtot Co and the creator of Solace Wellness Centre, I have spent years exploring how environment, movement and mindfulness contribute to a balanced, fulfilling life.</p>
  </div>
  <div class="abs copy" style="left:374px;top:246px;width:108px">
    <p>I bring that same perspective into real estate — helping buyers discover properties that elevate their everyday lifestyle, and helping sellers position their homes through the lens <b>of restoration, space and wellbeing.</b></p>
    <p class="italic-line" style="font-size:6.2px;margin-top:6px">“Because a truly extraordinary home doesn't just shelter life — it enhances it.”</p>
  </div>
</section>

<!-- Spread: difference + every home has a story -->
<section class="spread" style="left:59px;top:909px;width:490px;height:340px">
  <div class="page light" style="left:0;top:0;width:246px;height:282px">
    <h2 class="abs title" style="left:17px;top:17px;font-size:16px">THE MAREN HOLT<br><em>DIFFERENCE</em></h2>
    <div class="photo" role="img" aria-label="Maren laughing while seated on a cream sofa" style="left:143px;top:47px;width:103px;height:210px;background:linear-gradient(170deg,#f3efe9,#ddd3c8)"></div>
    <div class="abs" style="left:17px;top:64px;width:118px">
      <div class="diff-item"><span class="num" style="font-size:6px">01</span><div><div class="label">Lifestyle</div><div class="copy">I look beyond the floor plan to understand how buyers will actually experience and live in the home.</div></div></div>
      <div class="diff-item"><span class="num" style="font-size:6px">02</span><div><div class="label">Wellness</div><div class="copy">Highlighting light, water, air, privacy and restorative features that resonate with modern high-net-worth buyers.</div></div></div>
      <div class="diff-item"><span class="num" style="font-size:6px">03</span><div><div class="label">Presentation</div><div class="copy">Curating magazine-grade visual staging and cinematic film to create an immediate emotional connection.</div></div></div>
      <div class="diff-item"><span class="num" style="font-size:6px">04</span><div><div class="label">Targeting</div><div class="copy">Connecting with qualified local, interstate and international buyers seeking an elevated lifestyle.</div></div></div>
      <div class="diff-item"><span class="num" style="font-size:6px">05</span><div><div class="label">Network</div><div class="copy">Leveraging the unmatched prestige reach and database power of the Fenwick Dale Coastline Group.</div></div></div>
      <div class="diff-item" style="margin-bottom:0"><span class="num" style="font-size:6px">06</span><div><div class="label">Negotiation</div><div class="copy">More than 20 years' commercial and residential deal experience driving premium competition.</div></div></div>
    </div>
  </div>
  <div class="page dark" style="left:0;top:282px;width:246px;height:58px">
    <div class="abs label gold" style="left:17px;top:12px;font-size:3.8px">The Strategic Outcome</div>
    <div class="abs copy" style="left:17px;top:20px;width:100px">Properties that stand out distinctly in buyer memory, commanding attention and setting benchmark values across the Amber Coast.</div>
    <p class="abs italic-line" style="left:125px;top:10px;width:110px;font-size:6.6px">“When strategy meets authentic lifestyle storytelling, we achieve outcomes ordinary campaigns cannot reach.”</p>
  </div>
  <div class="page dark" style="left:246px;top:0;width:244px;height:340px">
    <div class="photo" role="img" aria-label="Dark moody interior with timber and stone" style="left:0;top:0;width:244px;height:110px;background:linear-gradient(180deg,#3c4048 0%,#2a2d35 60%,var(--navy) 100%)"></div>
    <h2 class="abs title" style="left:17px;top:115px;font-size:15px">EVERY HOME HAS A<br><em>STORY</em></h2>
    <p class="abs italic-line" style="left:17px;top:158px;width:210px;font-size:12.5px;line-height:1.3">“My role is to discover what makes yours extraordinary.”</p>
    <div class="tile" style="left:17px;top:208px;width:66px;height:118px">
      <div class="num">01</div>
      <div class="label">What makes your property distinct?</div>
      <div class="copy">Is it the architectural vision, deep waterfront access, panoramic outlooks, secluded gardens, or the prestige and privacy of its address?</div>
    </div>
    <div class="tile" style="left:89px;top:208px;width:66px;height:118px">
      <div class="num">02</div>
      <div class="label">How does the home make you feel?</div>
      <div class="copy">A sanctuary of enduring calm, creative inspiration, effortless connection, or an extraordinary setting for entertaining and restorative living.</div>
    </div>
    <div class="tile" style="left:161px;top:208px;width:66px;height:118px">
      <div class="num">03</div>
      <div class="label">Who will fall in love with it?</div>
      <div class="copy">Discerning families, executives, downsizers seeking turnkey ease, avid boaties, golfers, and lifestyle buyers prioritising wellness and quality of life.</div>
    </div>
  </div>
</section>

<!-- Spread: my market + wellness home -->
<section class="spread" style="left:608px;top:906px;width:495px;height:347px">
  <div class="page dark" style="left:0;top:0;width:247px;height:347px">
    <div class="photo" role="img" aria-label="White waterfront home with palms under a blue sky" style="left:0;top:0;width:247px;height:120px;background:linear-gradient(180deg,#8fb6d8 0%,#c7d7e3 45%,#d9dcdc 70%,#5a6066 100%)"></div>
    <h2 class="abs title" style="left:17px;top:130px;font-size:15px">MY MARKET —<br><em>NORTHERN AMBER COAST</em></h2>
    <div class="tile" style="left:17px;top:180px;width:49px;height:44px;padding:5px"><div class="label" style="margin-top:0">Kestrel Isle</div><div class="copy">Deep Waterfront &amp; Links</div></div>
    <div class="tile" style="left:74px;top:180px;width:49px;height:44px;padding:5px"><div class="label" style="margin-top:0">Linden Cove</div><div class="copy">Gated Marina Resort</div></div>
    <div class="tile" style="left:131px;top:180px;width:49px;height:44px;padding:5px"><div class="label" style="margin-top:0">Ashvale</div><div class="copy">Riverfront &amp; Gated Enclaves</div></div>
    <div class="tile" style="left:188px;top:180px;width:49px;height:44px;padding:5px"><div class="label" style="margin-top:0">Waterfront Estates</div><div class="copy">Prestige Living</div></div>
    <div class="abs copy" style="left:17px;top:250px;width:110px">
      <p style="font-size:5.2px">I specialise in the lifestyle-driven property market of the Northern Amber Coast.</p>
      <p>From the waterfront homes and private enclaves of Kestrel Isle and Linden Cove to the established gated estates of Ashvale, I understand the lifestyle characteristics that attract buyers to this part of the coast.</p>
    </div>
    <div class="tile" style="left:137px;top:245px;width:100px;height:80px;padding:8px">
      <p class="italic-line" style="font-size:6.4px;color:var(--ink-light)">“Having personally experienced the lifestyle of these communities, I understand that buyers are often purchasing far more than a house.</p>
      <p class="italic-line" style="font-size:6.4px;color:var(--ink-light);margin-top:4px">They are buying a way of life.”</p>
    </div>
  </div>
  <div class="page light" style="left:247px;top:0;width:248px;height:347px">
    <div class="photo" role="img" aria-label="Bright spa bathroom with glass shower and stone vanity" style="left:0;top:0;width:248px;height:136px;background:linear-gradient(160deg,#e9e8e6 0%,#cfd1d2 55%,#8f8a85 100%)"></div>
    <h2 class="abs title" style="left:17px;top:144px;font-size:15px">WHAT MAKES A<br><em>WELLNESS HOME?</em></h2>
    <p class="abs italic-line" style="left:17px;top:180px;font-size:6.6px;color:var(--ink-mute)">“The most desirable luxury is often the way a home makes you feel.”</p>
    <div class="tile on-light" style="left:17px;top:200px;width:68px;height:66px"><div class="num">01</div><div class="label">Water</div><div class="copy">Private pools, deep-water pontoon moorings, marina access, and calming water outlooks.</div></div>
    <div class="tile on-light" style="left:90px;top:200px;width:68px;height:66px"><div class="num">02</div><div class="label">Nature</div><div class="copy">Expansive green spaces, mature landscaped gardens, tranquil reserve outlooks, and walking trails.</div></div>
    <div class="tile on-light" style="left:163px;top:200px;width:68px;height:66px"><div class="num">03</div><div class="label">Light</div><div class="copy">Abundant natural daylighting, optimal northern aspect orientation, and expansive open-plan volumes.</div></div>
    <div class="tile on-light" style="left:17px;top:272px;width:68px;height:64px"><div class="num">04</div><div class="label">Movement</div><div class="copy">Direct access to championship golf, boating waterways, boardwalks, and active outdoor recreation.</div></div>
    <div class="tile on-light" style="left:90px;top:272px;width:68px;height:64px"><div class="num">05</div><div class="label">Restoration</div><div class="copy">Dedicated home spa facilities, saunas, cold plunge baths, and private quiet retreat spaces.</div></div>
    <div class="tile on-light" style="left:163px;top:272px;width:68px;height:64px"><div class="num">06</div><div class="label">Connection</div><div class="copy">Generous entertaining terraces, alfresco dining pavilions, and seamless indoor–outdoor living.</div></div>
  </div>
</section>

<!-- Spread: selling experience + power of presentation -->
<section class="spread" style="left:59px;top:1350px;width:493px;height:346px">
  <div class="page dark" style="left:0;top:0;width:247px;height:346px">
    <div class="photo" role="img" aria-label="Floating staircase with an indoor palm" style="left:0;top:0;width:247px;height:105px;background:linear-gradient(180deg,#3f434b 0%,#2b2e36 65%,var(--navy) 100%)"></div>
    <h2 class="abs title" style="left:17px;top:108px;font-size:16px">THE SELLING<br><em>EXPERIENCE</em></h2>
    <p class="abs italic-line" style="left:17px;top:143px;width:215px;font-size:6.3px;color:var(--ink-soft)">“Every stage is executed with precision, discretion, and an unwavering focus on creating competitive momentum for your home.”</p>
    <div class="tile" style="left:17px;top:172px;width:67px;height:84px"><div class="num">01</div><div class="label">Discovery &amp; Strategy</div><div class="copy">Understanding your objectives, timeline, property highlights, and target buyer demographic.</div></div>
    <div class="tile" style="left:90px;top:172px;width:67px;height:84px"><div class="num">02</div><div class="label">Preparation &amp; Styling</div><div class="copy">Refining presentation to showcase the home's wellness, light, architectural space, and lifestyle.</div></div>
    <div class="tile" style="left:163px;top:172px;width:67px;height:84px"><div class="num">03</div><div class="label">Bespoke Marketing</div><div class="copy">High-end photography, cinematic video, lifestyle editorial, digital targeting, and Fenwick Dale database reach.</div></div>
    <div class="tile" style="left:17px;top:262px;width:67px;height:76px"><div class="num">04</div><div class="label">Buyer Engagement</div><div class="copy">Private viewings, qualified buyer appointments, and structured open home experiences.</div></div>
    <div class="tile" style="left:90px;top:262px;width:67px;height:76px"><div class="num">05</div><div class="label">Strategic Negotiation</div><div class="copy">Creating competitive tension among qualified purchasers to secure maximum market value.</div></div>
    <div class="tile" style="left:163px;top:262px;width:67px;height:76px"><div class="num">06</div><div class="label">Settlement &amp; Beyond</div><div class="copy">Managing contracts, building inspections, finance milestones, and a seamless handover.</div></div>
  </div>
  <div class="page dark" style="left:247px;top:0;width:246px;height:346px">
    <div class="photo" role="img" aria-label="Styled living room with gallery wall and leather chairs" style="left:0;top:0;width:246px;height:118px;background:linear-gradient(160deg,#d9d2c8 0%,#a99a88 50%,#5e5348 100%)"></div>
    <h2 class="abs title" style="left:17px;top:128px;font-size:16px">THE POWER OF<br><em>PRESENTATION</em></h2>
    <p class="abs italic-line" style="left:17px;top:166px;width:215px;font-size:6.3px;color:var(--ink-soft)">“In luxury real estate, presentation is not simply decoration — it is positioning.”</p>
    <div class="abs label" style="left:17px;top:205px;width:100px">First impressions are everything</div>
    <div class="abs copy" style="left:17px;top:220px;width:100px">The way a home is styled, lit, photographed and presented online directly influences the calibre of buyers it attracts and the value they place on it.</div>
    <p class="abs italic-line" style="left:17px;top:260px;width:95px;font-size:6.3px;color:var(--ink-soft)">“My goal is to present every home so that buyers do not just see a property — they envision their life there.”</p>
    <div class="abs service-grid" style="left:125px;top:200px;width:105px">
      <div class="tile"><span class="label gold">01</span><span class="label">Professional styling advice</span></div>
      <div class="tile"><span class="label gold">02</span><span class="label">Architectural &amp; twilight photography</span></div>
      <div class="tile"><span class="label gold">03</span><span class="label">Cinematic lifestyle video</span></div>
      <div class="tile"><span class="label gold">04</span><span class="label">Drone &amp; waterway footage</span></div>
      <div class="tile"><span class="label gold">05</span><span class="label">Bespoke property monographs</span></div>
      <div class="tile"><span class="label gold">06</span><span class="label">Targeted digital &amp; social campaigns</span></div>
    </div>
  </div>
</section>

<!-- Spread: proven results + personal service -->
<section class="spread" style="left:605px;top:1350px;width:493px;height:346px">
  <div class="page" style="left:0;top:0;width:247px;height:346px;background:var(--paper);color:var(--ink-dark)">
    <h2 class="abs title" style="left:17px;top:17px;font-size:16px">PROVEN <em>RESULTS</em></h2>
    <div class="photo" role="img" aria-label="Waterfront home lit at dusk" style="left:17px;top:44px;width:104px;height:84px;background:linear-gradient(170deg,#3c4556,#1e2430)"><span class="label price-tag">$3,850,000</span></div>
    <div class="photo" role="img" aria-label="Bright open-plan living area" style="left:128px;top:44px;width:104px;height:84px;background:linear-gradient(170deg,#e7e3de,#a39c93)"><span class="label price-tag">$2,900,000</span></div>
    <div class="abs" style="left:17px;top:134px;width:104px"><div class="label">North Luxury Waterfront</div><div class="label gold" style="font-size:3.6px">Kestrel Isle Resort</div><div class="copy"><b>Sold in 34 days</b><br>Bespoke campaign positioning highlighting deep-water pontoon mooring and private wellness master suite.</div></div>
    <div class="abs" style="left:128px;top:134px;width:104px"><div class="label">The Anchorage Residence</div><div class="label gold" style="font-size:3.6px">Linden Cove</div><div class="copy"><b>Sold prior to auction</b><br>Strategic lifestyle videography attracting executive interstate buyers seeking immediate turnkey resort luxury.</div></div>
    <div class="photo" role="img" aria-label="Riverfront home with pool and palms" style="left:17px;top:195px;width:104px;height:84px;background:linear-gradient(170deg,#7a8da0,#3c4a40)"><span class="label price-tag">$2,150,000</span></div>
    <div class="photo" role="img" aria-label="Contemporary fairway villa at twilight" style="left:128px;top:195px;width:104px;height:84px;background:linear-gradient(170deg,#2f3340,#191c24)"><span class="label price-tag">$3,200,000</span></div>
    <div class="abs" style="left:17px;top:285px;width:104px"><div class="label">Riverfront Reserve Enclave</div><div class="label gold" style="font-size:3.6px">Ashvale Prestige</div><div class="copy"><b>Street record price</b><br>Targeted digital campaign articulating nature-immersed living, expansive alfresco pavilions, and total privacy.</div></div>
    <div class="abs" style="left:128px;top:285px;width:104px"><div class="label">The Pines Fairway Villa</div><div class="label gold" style="font-size:3.6px">Linden Cove</div><div class="copy"><b>Sold in 14 days</b><br>Direct database engagement connecting international purchasers with a private resort-inspired lifestyle estate.</div></div>
  </div>
  <div class="page dark" style="left:247px;top:0;width:246px;height:346px">
    <div class="photo" role="img" aria-label="Dining space with staircase and indoor palm" style="left:0;top:0;width:246px;height:105px;background:linear-gradient(180deg,#43464d 0%,#2b2e36 65%,var(--navy) 100%)"></div>
    <h2 class="abs title" style="left:17px;top:112px;font-size:15px">PERSONAL SERVICE.<br><em>NATIONAL REACH.</em></h2>
    <div class="tile" style="left:17px;top:154px;width:67px;height:86px"><div class="num">01</div><div class="label">Powerful Buyer Database</div><div class="copy">Direct access to qualified local, interstate, and international high-net-worth buyers actively looking for coastal luxury.</div></div>
    <div class="tile" style="left:90px;top:154px;width:67px;height:86px"><div class="num">02</div><div class="label">Luxury Property Marketing</div><div class="copy">Bespoke campaign production, cinematic lifestyle videography, and premier editorial syndication across leading property portals.</div></div>
    <div class="tile" style="left:163px;top:154px;width:67px;height:86px"><div class="num">03</div><div class="label">Auction Expertise</div><div class="copy">Industry-leading auctioneers driving competitive bidding environments that consistently outperform private treaty sales.</div></div>
    <div class="tile" style="left:17px;top:246px;width:67px;height:88px"><div class="num">04</div><div class="label">Digital Reach</div><div class="copy">Targeted multi-channel digital advertising and algorithmic social campaigns engaging passive and interstate buyers.</div></div>
    <div class="tile" style="left:90px;top:246px;width:67px;height:88px"><div class="num">05</div><div class="label">Local Knowledge</div><div class="copy">Decades of collective market intelligence, vetted sales history, and deep community relationships across the Northern Amber Coast.</div></div>
    <div class="tile" style="left:163px;top:246px;width:67px;height:88px"><div class="num">06</div><div class="label">National Network</div><div class="copy">Over 1,000 collaborating offices nationwide, seamlessly channelling executive interstate migration to our region.</div></div>
  </div>
</section>

<!-- Spread: promise + closing -->
<section class="spread" style="left:59px;top:1761px;width:507px;height:359px">
  <div class="page dark" style="left:0;top:0;width:254px;height:359px">
    <div class="photo" role="img" aria-label="Modern two-storey home at dusk with warm lights" style="left:0;top:0;width:254px;height:135px;background:linear-gradient(180deg,#3d424b 0%,#2a2e37 55%,var(--navy) 100%)"></div>
    <h2 class="abs title" style="left:17px;top:135px;font-size:16px">MY <em>PROMISE</em> TO YOU</h2>
    <p class="abs italic-line" style="left:17px;top:155px;font-size:6.3px;color:var(--ink-soft)">“Six foundational commitments you receive at every step of your selling journey.”</p>
    <div class="tile" style="left:17px;top:174px;width:69px;height:72px"><div class="num">01</div><div class="label">Transparency</div><div class="copy">Clear advice, honest feedback, and realistic expectations with no unnecessary promises.</div></div>
    <div class="tile" style="left:92px;top:174px;width:69px;height:72px"><div class="num">02</div><div class="label">Communication</div><div class="copy">You will know what is happening at every milestone throughout your entire campaign.</div></div>
    <div class="tile" style="left:167px;top:174px;width:69px;height:72px"><div class="num">03</div><div class="label">Strategy</div><div class="copy">Every decision is custom-engineered around your property, target market, and financial objectives.</div></div>
    <div class="tile" style="left:17px;top:252px;width:69px;height:72px"><div class="num">04</div><div class="label">Attention to Detail</div><div class="copy">Your home deserves meticulous preparation, thoughtful styling, and flawless presentation.</div></div>
    <div class="tile" style="left:92px;top:252px;width:69px;height:72px"><div class="num">05</div><div class="label">Personal Service</div><div class="copy">You deal directly with me personally — never handed off to junior assistants.</div></div>
    <div class="tile" style="left:167px;top:252px;width:69px;height:72px"><div class="num">06</div><div class="label">Result Focus</div><div class="copy">My primary role is to create the strongest possible environment for a record outcome.</div></div>
    <p class="abs italic-line" style="left:17px;top:330px;width:220px;text-align:center;font-size:6.3px;color:var(--ink-soft)">“Integrity, clear communication, and meticulous execution are not just principles — they are the standard for every property I represent.”</p>
  </div>
  <div class="page" role="img" aria-label="Faint dusk photograph of a luxury home behind the closing note" style="left:254px;top:0;width:253px;height:359px;background:radial-gradient(ellipse at 50% 45%,#2c3039 0%,#1d2028 55%,var(--navy-deep) 100%)"></div>
  <div class="abs" style="left:254px;top:0;width:253px;height:359px;text-align:center">
    <div class="label" style="position:absolute;left:0;top:30px;width:253px;font-size:3.6px;letter-spacing:.32em;color:var(--ink-soft)">A Personal Note</div>
    <h2 class="title" style="position:absolute;left:0;top:42px;width:253px;font-size:22px;color:var(--ink-light)">YOUR HOME. <em>YOUR</em><br><em>NEXT CHAPTER.</em></h2>
    <p class="serif" style="position:absolute;left:22px;top:120px;width:209px;font-size:9.5px;line-height:1.45;color:var(--ink-soft)">Selling a home is rarely just a transaction. It is the closing of one chapter and the beginning of another.</p>
    <p class="copy" style="position:absolute;left:22px;top:170px;width:209px;font-size:5px;color:var(--ink-soft)">My role is to make the journey feel considered, strategic and personal — while creating the strongest possible opportunity for your property in the marketplace.</p>
    <div style="position:absolute;left:126px;top:205px;width:1px;height:22px;background:var(--ink-soft);opacity:.5"></div>
    <div class="label" style="position:absolute;left:20px;top:236px;width:213px;font-size:4px;letter-spacing:.25em">Thank you for considering me to represent your home.</div>
    <p class="italic-line" style="position:absolute;left:20px;top:258px;width:213px;font-size:15px;line-height:1.3;color:var(--ink-light)">“I would be honoured to tell its story.”</p>
  </div>
</section>

<!-- Back cover -->
<section class="page" style="left:608px;top:2181px;width:244px;height:365px">
  <div class="photo" role="img" aria-label="Dark twilight photograph of a waterfront home" style="left:0;top:0;width:244px;height:365px;background:linear-gradient(180deg,#1f222a 0%,#1a1d24 55%,#23262e 100%)"></div>
  <div class="abs title" style="left:0;top:96px;width:244px;text-align:center;font-size:16px;letter-spacing:.12em;color:var(--ink-light)">MAREN HOLT</div>
  <div class="abs label" style="left:0;top:121px;width:244px;text-align:center;font-size:3.8px;font-weight:500;letter-spacing:.3em;color:var(--ink-soft)">Luxury Wellness Property</div>
  <div class="abs label" style="left:0;top:133px;width:244px;text-align:center;font-size:3.6px;letter-spacing:.3em;color:var(--ink-light)">Property · Wellness · Lifestyle</div>
  <div class="abs" style="left:0;top:148px;width:244px;text-align:center;font-size:7px;font-weight:500;letter-spacing:.05em;color:var(--ink-light)">0412 557 830</div>
  <div class="abs label" style="left:0;top:167px;width:244px;text-align:center;font-size:3.2px;font-weight:500;letter-spacing:.25em;color:var(--ink-mute)">Kestrel Isle · Linden Cove · Ashvale</div>
  <div class="abs" style="left:0;top:183px;width:244px;text-align:center;font-size:7px;font-weight:700;color:var(--ink-light)">Fenwick Dale</div>
  <div class="abs" style="left:0;top:195px;width:244px;text-align:center;font-size:3.4px;color:var(--ink-mute)">Fenwick Dale Coastline Group</div>
</section>

</body>
</html>
```